I need a newspaper ads that suits events / outings all over the world. refreshing feeling that suits my company logo.
Size of the ads is 6cm by 6cm a square
takenote
1) Joining up as members is free .
2) Places of interest tickets discount for members
3) Special events / outings host almost everyday
4) main point is everyone able to know each another
website : www.WandermoorHub.com
Target Market(s)
Targeting general age 18-40 . mainly singles
contents to put inside the ads
2) Local Places of interest tickets discount for members
4) Website : www.WandermoorHub.com
5) We also host photos contest
6) Meet the different faces of the world
7) Experience Sharing Gathering !
Industry/Entity Type
It Company
Requirements
Must have
- Refreshing feeling , and professional . will be uploading more pictures , kindly put some pictures combine into it to make people feel there is a lot activities can be involve when they join as member.

```html
<!DOCTYPE html>
<html lang="en">
<head>
<meta charset="utf-8">
<title>Wandermoor Hub – Newspaper Ad</title>
<link href="https://fonts.googleapis.com/css2?family=PT+Sans+Narrow:wght@400;700&family=Oswald:wght@500&display=swap" rel="stylesheet">
<style>
  :root {
    --backdrop: #d9dadb;
    --paper: #ffffff;
    --ink-grey: #4a4a4a;
    --brand-navy: #1a5a86;
    --brand-blue: #0d6ea3;
    --brand-sky: #29a8dc;
    --leaf-light: #6f9a5a;
    --leaf-dark: #2f4f2c;
    --lawn: #7fa663;
    --logo-grey: #8e9499;
  }
  * { box-sizing: border-box; margin: 0; padding: 0; }
  html, body {
    width: 1200px; height: 900px; overflow: hidden;
    background: var(--backdrop);
  }
  .canvas { position: relative; width: 1200px; height: 900px; }
  .ad {
    position: absolute; left: 255px; top: 105px;
    width: 690px; height: 690px;
    background: var(--paper);
    box-shadow: 0 2px 10px rgba(0,0,0,.18);
    overflow: hidden;
  }
  .photo {
    position: absolute; width: 196px; height: 196px;
    background: linear-gradient(160deg, var(--leaf-light), var(--leaf-dark));
  }
  .photo--group { left: 29px; top: 36px; border-top-left-radius: 70px; }
  .photo--pair { left: 247px; top: 36px; }
  .photo--guide { left: 465px; top: 36px; border-top-right-radius: 70px; }
  .photo--huddle {
    left: 465px; top: 247px; border-bottom-right-radius: 80px;
    background: linear-gradient(180deg, var(--leaf-light) 0%, var(--lawn) 45%, #5a7d4a 100%);
  }
  .perks {
    position: absolute; left: 30px; top: 254px; width: 420px;
    list-style: none;
    font-family: "PT Sans Narrow", sans-serif;
    font-size: 22px; line-height: 26px; color: var(--ink-grey);
  }
  .perks li { position: relative; padding-left: 12px; margin-bottom: 9px; }
  .perks li::before { content: "•"; position: absolute; left: 0; }
  .headline { position: absolute; left: 0; top: 0; width: 690px; height: 690px; }
  .headline text {
    font-family: "Oswald", sans-serif; font-weight: 500; font-size: 74px;
  }
  .website {
    position: absolute; left: 30px; top: 644px;
    font-family: "PT Sans Narrow", sans-serif; font-size: 24px;
    color: var(--ink-grey);
  }
  .brand {
    position: absolute; left: 340px; top: 612px;
    display: flex; align-items: center; gap: 14px;
  }
  .brand__dot {
    width: 76px; height: 76px; border-radius: 50%;
    background: var(--logo-grey);
  }
  .brand__name {
    font-family: "PT Sans Narrow", sans-serif; font-weight: 700;
    font-size: 36px; letter-spacing: 1px; color: var(--brand-navy);
  }
</style>
</head>
<body>
<div class="canvas">
  <section class="ad">
    <div class="photo photo--group" role="img" aria-label="Photo of three young members sitting among tropical plants"></div>
    <div class="photo photo--pair" role="img" aria-label="Photo of two members resting on a bench in a garden"></div>
    <div class="photo photo--guide" role="img" aria-label="Photo of a guide talking to the group in a garden"></div>
    <div class="photo photo--huddle" role="img" aria-label="Photo of a group of friends joining hands in a park"></div>

    <ul class="perks">
      <li>Joining up as members is free</li>
      <li>Local Places of interest tickets discount for members</li>
      <li>Special events / outings host almost everyday</li>
      <li>We also host photos contest</li>
      <li>Meet the different faces of the world</li>
      <li>Experience Sharing Gathering !</li>
    </ul>

    <svg class="headline" viewBox="0 0 690 690" aria-label="The gate to the new world">
      <defs>
        <linearGradient id="headline-fill" x1="0" y1="0" x2="1" y2="0">
          <stop offset="0" stop-color="var(--brand-sky)"/>
          <stop offset="1" stop-color="var(--brand-blue)"/>
        </linearGradient>
        <linearGradient id="swoosh-fill" x1="0" y1="0" x2="1" y2="0">
          <stop offset="0" stop-color="var(--brand-sky)"/>
          <stop offset="1" stop-color="var(--brand-blue)"/>
        </linearGradient>
        <path id="headline-curve" d="M 24 568 C 200 560, 420 540, 676 526"/>
      </defs>
      <text fill="url(#headline-fill)">
        <textPath href="#headline-curve" textLength="650" lengthAdjust="spacingAndGlyphs">THE GATE TO THE NEW WORLD</textPath>
      </text>
      <path d="M 0 590 C 180 600, 420 560, 690 576 L 690 582 C 420 570, 200 620, 0 606 Z" fill="url(#swoosh-fill)"/>
    </svg>

    <p class="website">www.WandermoorHub.com</p>

    <div class="brand">
      <span class="brand__dot"></span>
      <span class="brand__name">VELORIA EVENTS</span>
    </div>
  </section>
</div>
</body>
</html>
```